Mara Quill
Senior Administrator
Modern
P.O. Box 742
Larkfield, NJ
bwsaquill@postlark.com
www.thebrightwaystudyacademy.com
please use this on front of card

```html
<!DOCTYPE html>
<html lang="en">
<head>
<meta charset="utf-8">
<title>Mara Quill – Business Card</title>
<link href="https://fonts.googleapis.com/css2?family=Russo+One&family=Cinzel:wght@500&family=Tinos&display=swap" rel="stylesheet">
<style>
  :root {
    --stage: #000000;
    --card-white: #ffffff;
    --card-grey: #cfcfd1;
    --brand-blue: #1d4fa3;
    --brand-red: #d8262c;
    --ink: #111111;
    --fine: #333333;
  }
  * { margin: 0; padding: 0; box-sizing: border-box; }
  html, body { width: 1200px; height: 872px; overflow: hidden; background: var(--stage); }
  .canvas { position: relative; width: 1200px; height: 872px; background: var(--stage); }
  .card { position: absolute; left: 266px; width: 594px; height: 342px; overflow: hidden; background: var(--card-white); }
  .card--front { top: 72px; }
  .card--back { top: 444px; }
  .card__bg { position: absolute; inset: 0; width: 100%; height: 100%; }
  .name { position: absolute; font-family: "Russo One", sans-serif; font-weight: 400; letter-spacing: 1px; line-height: 1; white-space: nowrap; }
  .details { position: absolute; font-family: "Tinos", serif; color: var(--fine); line-height: 1.25; white-space: nowrap; }
  .brand { position: absolute; display: flex; align-items: center; gap: 16px; }
  .brand__dot { width: 80px; height: 80px; border-radius: 50%; background: var(--brand-red); flex: none; }
  .brand__name { font-family: "Cinzel", serif; font-weight: 500; color: var(--brand-blue); font-size: 28px; line-height: 1.1; white-space: nowrap; }

  .card--front .name { left: 39px; top: 82px; font-size: 38px; color: var(--brand-blue); }
  .card--front .details { left: 41px; top: 126px; font-size: 8px; }
  .card--front .brand { left: 230px; top: 168px; }

  .card--back .name { left: 306px; top: 90px; font-size: 46px; color: var(--ink); }
  .card--back .details { left: 420px; top: 150px; font-size: 10px; }
  .card--back .brand { left: 62px; top: 160px; }
  .card--back .web { position: absolute; left: 31px; top: 282px; font-family: "Tinos", serif; font-size: 9px; color: var(--fine); line-height: 1.25; white-space: nowrap; }
</style>
</head>
<body>
<main class="canvas">
  <section class="card card--front">
    <svg class="card__bg" viewBox="0 0 594 342" preserveAspectRatio="none" aria-hidden="true">
      <path d="M0 0 H594 V92 C500 110 430 160 330 200 C220 245 110 250 0 240 Z" fill="var(--card-grey)"/>
    </svg>
    <h1 class="name">Mara Quill</h1>
    <p class="details">Senior Administrator<br>P.O. Box 742 Larkfield, NJ 08517 Toll free: 800.555.0142</p>
    <div class="brand">
      <span class="brand__dot"></span>
      <span class="brand__name">Brightway<br>Study Academy</span>
    </div>
  </section>

  <section class="card card--back">
    <svg class="card__bg" viewBox="0 0 594 342" preserveAspectRatio="none" aria-hidden="true">
      <path d="M0 0 H594 V30 C470 30 380 60 300 80 C200 105 100 95 0 70 Z" fill="var(--card-grey)"/>
      <path d="M594 342 H380 C450 320 520 260 594 200 Z" fill="var(--card-grey)"/>
    </svg>
    <h2 class="name">Mara Quill</h2>
    <p class="details">Senior Administrator<br>P.O. Box 742<br>Larkfield, NJ<br>08517<br>Toll free: 800.555.0142</p>
    <div class="brand">
      <span class="brand__dot"></span>
      <span class="brand__name">Brightway<br>Study Academy</span>
    </div>
    <p class="web">bwsaquill@postlark.com<br>www.thebrightwaystudyacademy.com</p>
  </section>
</main>
</body>
</html>
```